Flyer Design Project

Training and Consulting Flyer

I attached a document that contained the wording for the flyer as well as the logo.

Target Market(s)

Willow Crest agencies and grantees

Industry/Entity Type

Training

Font styles to use
Sans Serif

Colors
e667a6
eda3c7
a54499
b768aa
f9d9e8

Requirements
Must have
• Words provided on attachment
Nice to have
• Graphics that are related to adult training/learning and consulting

```html
<!DOCTYPE html>
<html lang="en">
<head>
<meta charset="utf-8">
<title>Lumen Health Advisors – Flyer and Cover</title>
<link href="https://fonts.googleapis.com/css2?family=Roboto+Condensed:wght@400;700&family=Montserrat:wght@400&display=swap" rel="stylesheet">
<style>
  :root{
    --magenta:#b01f6e;
    --magenta-deep:#8e1a5c;
    --pink-soft:#eda3c7;
    --blush:#f9d9e8;
    --orchid:#b768aa;
    --plum:#a54499;
    --ink:#141414;
    --paper:#ffffff;
    --backdrop:#e4e4e6;
  }
  *{box-sizing:border-box;margin:0;padding:0}
  html,body{width:1200px;height:1200px;overflow:hidden}
  body{background:var(--backdrop);font-family:"Roboto Condensed",sans-serif;color:var(--ink);position:relative}

  /* ---------- Flyer ---------- */
  .flyer{position:absolute;left:22px;top:20px;width:578px;height:742px;background:var(--paper);box-shadow:0 4px 14px rgba(0,0,0,.25);overflow:hidden}
  .flyer__band{position:absolute;left:0;top:34px;width:100%;height:124px;background:var(--magenta)}
  .flyer__brand{position:absolute;left:35px;top:34px;width:235px;height:124px;background:var(--paper);display:flex;flex-direction:column;align-items:center;justify-content:center;gap:10px}
  .brand-name{display:flex;align-items:center;gap:8px;font-weight:700;font-size:25px;line-height:1;color:var(--ink);text-transform:uppercase}
  .brand-name__dot{width:14px;height:14px;border-radius:50%;background:var(--magenta);flex:none}
  .tagline{font-family:"Montserrat",sans-serif;font-size:13px;letter-spacing:.5px;color:var(--ink)}
  .flyer__program{position:absolute;left:270px;top:34px;width:308px;height:124px;display:flex;flex-direction:column;align-items:center;justify-content:center;color:var(--paper);text-align:center}
  .program-name{font-size:34px;font-weight:700;line-height:1}
  .program-sub{font-size:14px;margin-top:10px}

  .flyer__headline{position:absolute;left:0;top:180px;width:100%;text-align:center;font-size:18px;line-height:1.3}
  .flyer__headline em{font-style:italic;font-weight:700;color:var(--magenta)}
  .rule{position:absolute;height:4px;background:var(--magenta)}
  .rule--top{left:0;top:246px;width:450px}
  .rule--bottom{left:216px;top:388px;width:362px}

  .photo{position:absolute;top:252px;height:136px}
  .photo--family{left:0;width:177px;background:linear-gradient(135deg,#9fbf6a,#e8c9a8 55%,#c9a07b)}
  .photo--kids{left:186px;width:190px;background:linear-gradient(160deg,#f4e6d6,#e9a35c 50%,#7fb34e)}
  .photo--fitness{left:385px;width:193px;background:linear-gradient(120deg,#e9e4df,#d7c3b4 40%,#6d8fb0 70%,#8fd08c)}

  .flyer__intro{position:absolute;left:41px;top:413px;width:500px;font-size:13.5px;font-weight:700;line-height:1.25}
  .services{position:absolute;left:38px;top:462px;width:510px;list-style:none}
  .services li{display:flex;gap:10px;font-size:11px;line-height:1.25;margin-bottom:13px}
  .services li::before{content:"";flex:none;width:12px;height:12px;border-radius:50%;border:2px solid var(--magenta);margin-top:3px}

  .flyer__footer{position:absolute;left:0;top:630px;width:100%;height:112px;background:var(--magenta);border-top:4px solid var(--ink);color:var(--paper)}
  .contact-person{position:absolute;left:41px;top:26px;font-size:27px}
  .contact-person small{font-size:15px;margin-left:6px}
  .contact-divider{position:absolute;left:235px;top:8px;width:1px;height:60px;background:var(--paper)}
  .contact-list{position:absolute;left:252px;top:4px;list-style:none;font-size:13px}
  .contact-list li{display:flex;align-items:center;gap:10px;height:23px}
  .contact-list svg{width:12px;height:12px;fill:var(--paper);flex:none}

  /* ---------- Cover ---------- */
  .cover{position:absolute;left:614px;top:404px;width:578px;height:746px;box-shadow:0 4px 14px rgba(0,0,0,.25);overflow:hidden}
  .cover__art{position:absolute;inset:0;background:radial-gradient(ellipse at 50% 55%,#fff6e8 0%,#f1d9d6 30%,#c79bb9 65%,#8f5f8c 100%)}
  .cover__brand{position:absolute;left:0;top:115px;width:100%;display:flex;flex-direction:column;align-items:center;gap:14px}
  .cover__brand .brand-name{font-size:40px}
  .cover__brand .brand-name__dot{width:20px;height:20px}
  .cover__brand .tagline{font-size:18px}
  .cover__title{position:absolute;left:200px;top:500px;width:320px;text-align:center}
  .cover__title .program-name{color:var(--magenta-deep);font-size:44px}
  .cover__sub{font-weight:700;font-size:18px;line-height:1.3;margin-top:14px}
  .cover__person{font-size:17px;margin-top:20px}
  .cover__person small{font-size:10px;margin-left:4px}
</style>
</head>
<body>

<section class="flyer">
  <div class="flyer__band"></div>
  <div class="flyer__brand">
    <div class="brand-name"><span class="brand-name__dot"></span>Lumen Health Advisors</div>
    <div class="tagline">TOGETHER WE CAN</div>
  </div>
  <div class="flyer__program">
    <div class="program-name">Insight Metrics</div>
    <div class="program-sub">Health Consultants &amp; Group</div>
  </div>

  <h1 class="flyer__headline" style="font-weight:400">Innovative Approaches to meeting the 5 year funding measures<br>in the content area of <em>Health, Nutrition, Oral Health &amp; Safety</em></h1>
  <div class="rule rule--top"></div>

  <div class="photo photo--family" role="img" aria-label="Smiling family of parents and children outdoors"></div>
  <div class="photo photo--kids" role="img" aria-label="Group of cheerful children posing together"></div>
  <div class="photo photo--fitness" role="img" aria-label="Women stretching in a fitness class"></div>
  <div class="rule rule--bottom"></div>

  <p class="flyer__intro">Lumen Health Advisors has embarked on a new methodology deigned ensure programs meet total requirements as prescribed under the health Services program.</p>
  <ul class="services">
    <li>Let us manage your health tips program through remote and offsite measures to ensure total compliance and strategic methodology toward quality service approaches.</li>
    <li>Let us provide consultants to mentor your health manager nutrition content specialist facilities safety manager these support consultant are advanced level academies in their specialized areas of focus.</li>
    <li>Let us provide advanced based Mock Reviews for your program designed to assist management staff in focus I, Focus II Review strategies for 2018.</li>
    <li>Let us provide T/ TA for any new Health, Nutrition and Safety staff to ensure they are fully prepared to perform their job duties at their highest level of management approaches.</li>
  </ul>

  <footer class="flyer__footer">
    <div class="contact-person">Dana Reyes<small>CEO</small></div>
    <div class="contact-divider"></div>
    <ul class="contact-list">
      <li><svg viewBox="0 0 12 12"><circle cx="6" cy="6" r="5" fill="none" stroke="#fff" stroke-width="1.6"/><circle cx="6" cy="6" r="2"/></svg>lumenhealthadvisors@example.com</li>
      <li><svg viewBox="0 0 12 12"><path d="M2 1h3l1 3-2 1c1 2 2 3 3 3l1-2 3 1v3c-6 0-9-3-9-9z"/></svg>(555) 014-2290</li>
      <li><svg viewBox="0 0 12 12"><path d="M6 0a4 4 0 0 0-4 4c0 3 4 8 4 8s4-5 4-8a4 4 0 0 0-4-4zm0 5.5A1.5 1.5 0 1 1 6 2.5a1.5 1.5 0 0 1 0 3z"/></svg>P.O. Box 482 Maplewood, GA 30000</li>
    </ul>
  </footer>
</section>

<section class="cover">
  <div class="cover__art" role="img" aria-label="Silhouetted hands reaching toward butterflies in a glowing pink sky"></div>
  <div class="cover__brand">
    <div class="brand-name"><span class="brand-name__dot"></span>Lumen Health Advisors</div>
    <div class="tagline">TOGETHER WE CAN</div>
  </div>
  <div class="cover__title">
    <div class="program-name">Insight Metrics</div>
    <div class="cover__sub">Health Consultants<br>&amp; Group</div>
    <div class="cover__person">Dana Reyes<small>CEO</small></div>
  </div>
</section>

</body>
</html>
```